creative design for packing box of 3D paper puzzle

We want to get a packaging box design for the 3D puzzle. The packaging is for animal puzzles, like birds, insect ,wild animal. it is for young chirdren. 5-12 years old.
The box size : 12*17*2CM, 2.5CM header. Attach is some packing design ideal and our logo.
We like more nice design. It can attract the eyes. We hope all items can be use same background, and just change the color and put different animal photo on it. Box is same design, you can check the file “box-different color” . same design, just diffirent color, photo, text..
Please send us your design in diffirent color. Also You can visit our website: www.tovelk.com. you can kow how about our product.
We attach 3 items photo. You can choose one to make the designon. Our product is DIY, education. Animal with scene
Target Market(s)
Europe,Janpan,USA
Colors
Designer to choose colors to be used in the design.
Requirements
Must have
- our Logo, some nice text or signo
Nice to have
- nice background

```html
<!DOCTYPE html>
<html lang="en">
<head>
<meta charset="utf-8">
<title>3D Paper Puzzle – Packaging</title>
<link href="https://fonts.googleapis.com/css2?family=Fredoka:wght@500;700&family=Roboto:wght@400&display=swap" rel="stylesheet">
<style>
  :root {
    --bg: #eef3f8;
    --indigo: #3b3a8f;
    --indigo-dark: #2f2e78;
    --paper: #f2f2f2;
    --red: #e02a30;
    --green: #8cc63f;
    --orange: #ec7f2b;
    --grey-dot: #a9a9ad;
    --white: #ffffff;
    --ink: #2a2a2a;
  }
  * { margin: 0; padding: 0; box-sizing: border-box; }
  html, body { width: 1200px; height: 1200px; overflow: hidden; background: var(--bg); }
  .canvas { position: relative; width: 1200px; height: 1200px; }

  .box { position: absolute; left: 320px; top: 150px; width: 560px; }

  .header {
    position: relative; height: 118px; background: var(--indigo);
    display: flex; align-items: center; justify-content: space-between; padding: 0 22px;
  }
  .header__item { width: 66px; text-align: center; color: var(--white);
    font: 400 10px/1.1 "Roboto", sans-serif; text-transform: uppercase; }
  .header__dot { width: 50px; height: 50px; border-radius: 50%; background: var(--grey-dot); margin: 0 auto 8px; }
  .header__pair { display: flex; gap: 26px; }
  .hang-hole { position: relative; width: 126px; height: 32px; border-radius: 16px; background: #7ec4f0; margin-top: 18px; }
  .hang-hole::before { content: ""; position: absolute; left: 50%; top: -12px; width: 24px; height: 24px;
    margin-left: -12px; border-radius: 50%; background: #7ec4f0; }

  .front { position: relative; height: 793px; overflow: hidden;
    background: linear-gradient(160deg, var(--paper), #e6e6e6); }
  .front__pattern { position: absolute; inset: 0;
    background: linear-gradient(160deg, #f4f4f4 0%, #e4e4e4 100%); }
  .front__shapes { position: absolute; inset: 0; }

  .brand { position: absolute; right: 22px; top: 44px; display: flex; flex-direction: column; align-items: center; gap: 8px; }
  .brand__mark { width: 62px; height: 62px; border-radius: 50%; background: var(--indigo); }
  .brand__name { font: 700 24px/1 "Fredoka", sans-serif; color: var(--indigo); letter-spacing: 3px; }

  .title { position: absolute; left: 0; right: 0; top: 108px; text-align: center;
    font-family: "Fredoka", sans-serif; font-weight: 700; line-height: .82; }
  .title__3d { display: block; font-size: 78px; color: var(--red); text-shadow: 3px 3px 0 var(--ink); margin-left: 20px; }
  .title__paper { display: block; font-size: 92px; color: var(--indigo); text-shadow: 3px 3px 0 var(--red); margin-left: 60px; }
  .title__puzzle { display: block; font-size: 86px; color: var(--green); text-shadow: 3px 3px 0 var(--indigo); margin-left: 110px; }

  .product-photo { position: absolute; left: 80px; top: 330px; width: 400px; height: 370px;
    border-radius: 40% 40% 30% 30% / 35% 35% 20% 20%;
    background: radial-gradient(ellipse at 50% 55%, #a8d36a 0%, #7fae4a 35%, #c98a3c 65%, rgba(230,230,230,0) 75%); }

  .badge { position: absolute; left: -20px; top: 650px; width: 220px; height: 160px; border-radius: 50%;
    background: var(--red); box-shadow: inset 0 0 0 4px var(--red), inset 0 0 0 6px var(--white);
    color: var(--white); text-align: center; padding-top: 50px; padding-left: 18px; }
  .badge__title { font: 700 28px/1 "Fredoka", sans-serif; letter-spacing: 1px;
    border-bottom: 3px solid var(--white); display: inline-block; padding: 0 4px 4px; }
  .badge__age { font: 400 15px/1 "Roboto", sans-serif; margin-top: 8px; }
</style>
</head>
<body>
<main class="canvas">
  <section class="box">
    <header class="header">
      <div class="header__pair">
        <div class="header__item"><div class="header__dot"></div>Brief for product</div>
        <div class="header__item"><div class="header__dot"></div>Brief for product</div>
      </div>
      <div class="hang-hole"></div>
      <div class="header__pair">
        <div class="header__item"><div class="header__dot"></div>Brief for product</div>
        <div class="header__item"><div class="header__dot"></div>Brief for product</div>
      </div>
    </header>

    <div class="front">
      <div class="front__pattern" role="img" aria-label="Light grey grid of rounded squares background pattern"></div>
      <svg class="front__shapes" viewBox="0 0 560 793" width="560" height="793">
        <path fill="var(--indigo)" d="M0 0 H290 C270 25 250 50 190 55 C140 58 100 60 75 130 C55 200 40 240 0 275 Z"/>
        <path fill="var(--indigo)" d="M560 540 C510 555 480 600 460 700 C445 760 420 760 300 762 C260 762 250 780 250 793 H560 Z"/>
        <circle cx="148" cy="178" r="10" fill="var(--red)"/>
        <circle cx="382" cy="175" r="9" fill="var(--indigo)"/>
        <circle cx="340" cy="187" r="4" fill="var(--orange)"/>
        <circle cx="155" cy="122" r="3" fill="var(--indigo)"/>
        <circle cx="247" cy="110" r="4" fill="var(--orange)"/>
        <circle cx="415" cy="270" r="8" fill="var(--indigo)"/>
        <circle cx="96" cy="330" r="10" fill="var(--indigo)"/>
        <circle cx="440" cy="340" r="13" fill="var(--orange)"/>
        <circle cx="275" cy="345" r="4" fill="var(--orange)"/>
        <circle cx="345" cy="385" r="5" fill="var(--red)"/>
        <circle cx="386" cy="352" r="3" fill="var(--indigo)"/>
      </svg>

      <div class="brand">
        <div class="brand__mark"></div>
        <span class="brand__name">TOVELK</span>
      </div>

      <h1 class="title">
        <span class="title__3d">3D</span>
        <span class="title__paper">paper</span>
        <span class="title__puzzle">puzzle</span>
      </h1>

      <div class="product-photo" role="img" aria-label="Photo of the assembled green paper triceratops model standing on a brown base with palm trees"></div>

      <div class="badge">
        <div class="badge__title">DINOSAUR</div>
        <div class="badge__age">Suitable for 5-12 years</div>
      </div>
    </div>
  </section>
</main>
</body>
</html>
```